Plimbo.com re-design on Wix platform

Re-do this website : www.plimbo.com
Plimbo is a sound conditioner that uses the calming, sedative qualities of mundane rhythmic stimulation to allow its users to rest easier and deeper than they normally would.
I think of Plimbo.com as a web app; a place to use and buy the product. Im open to suggestion on site layouts, whether you use one page or several.
Use the same color scheme: purple, white, black, grey/silver
I would like a place for testimonials, even though you don't currently see one on the site. Other than that, assume the content will stay mostly the same.
I'd like a clean, modern, professional look. The site will reside on Wix platform.

```html
<!DOCTYPE html>
<html lang="en">
<head>
<meta charset="utf-8">
<title>Plimbo — Testimonials &amp; Contact</title>
<link rel="stylesheet" href="https://fonts.googleapis.com/css2?family=EB+Garamond:wght@400&family=Nunito+Sans:ital,wght@0,300;0,400;1,400&display=swap">
<style>
  :root {
    --purple: #a4049f;
    --black: #111111;
    --white: #ffffff;
    --field: #e4e4e4;
    --footer: #cbcbcb;
    --body-font: "Nunito Sans", Arial, sans-serif;
    --display-font: "EB Garamond", Georgia, serif;
  }
  * { box-sizing: border-box; margin: 0; padding: 0; }
  html, body { width: 1200px; height: 2209px; overflow: hidden; background: var(--white); }
  body { position: relative; font-family: var(--body-font); color: var(--black); }

  .eyebrow {
    position: absolute; left: 0; width: 1200px; text-align: center;
    color: var(--purple); font-size: 19px; letter-spacing: 2.5px; font-weight: 400;
  }
  .eyebrow::after {
    content: ""; display: block; width: 44px; height: 3px;
    background: var(--purple); margin: 9px auto 0;
  }

  .testimonials__title {
    position: absolute; top: 224px; left: 0; width: 1200px; text-align: center;
    font-family: var(--display-font); font-weight: 400; font-size: 54px; line-height: 1.2;
  }
  .slider-arrow { position: absolute; top: 404px; width: 42px; height: 76px; }
  .slider-arrow--prev { left: 86px; }
  .slider-arrow--next { left: 1067px; }

  .quote {
    position: absolute; top: 404px; left: 255px; width: 690px; text-align: center;
    font-size: 19px; line-height: 31.5px; font-weight: 400;
  }
  .quote__author {
    position: absolute; top: 519px; left: 645px; font-size: 19px;
  }

  .hero-photo {
    position: absolute; top: 671px; left: 0; width: 1200px; height: 473px;
    background: linear-gradient(100deg, #d9cfc3 0%, #3a2a22 22%, #5b4236 40%, #2b211d 55%, #cfc9c2 70%, #6d6f76 85%, #9a9ca3 100%);
  }

  .contact__intro {
    position: absolute; top: 1322px; left: 0; width: 1200px; text-align: center;
    font-size: 19px; line-height: 31px;
  }
  .contact-form { position: absolute; top: 1465px; left: 439px; width: 319px; }
  .field {
    display: block; width: 319px; background: var(--field); border: none;
    font-family: var(--body-font); font-size: 16px; color: #333;
    padding: 8px 10px; margin-bottom: 7px; height: 37px;
  }
  .field--message { height: 122px; margin-bottom: 6px; }
  .button {
    display: block; background: var(--purple); color: var(--white); border: none;
    font-family: var(--body-font); font-weight: 300; letter-spacing: 1px;
  }
  .button--send { width: 319px; height: 37px; font-size: 16px; }

  .back-to-top { position: absolute; top: 1730px; left: 1034px; width: 116px; text-align: center; }
  .back-to-top__icon { display: block; margin: 0 auto; width: 56px; height: 56px; }
  .back-to-top__label { display: block; margin-top: 8px; font-size: 14px; }

  .site-footer { position: absolute; top: 1841px; left: 0; width: 1200px; height: 368px; background: var(--footer); }
  .subscribe { position: absolute; top: 193px; left: 349px; display: flex; }
  .subscribe__input {
    width: 338px; height: 49px; border: none; background: var(--white);
    font-family: var(--body-font); font-size: 16px; padding: 0 17px; color: #333;
  }
  .button--subscribe { width: 164px; height: 49px; font-size: 20px; letter-spacing: 2px; font-weight: 400; }
  .copyright {
    position: absolute; top: 328px; left: 0; width: 1200px; text-align: center;
    font-size: 14px; font-style: italic;
  }
</style>
</head>
<body>
  <section class="testimonials">
    <h2 class="eyebrow" style="top:124px">TESTIMONIALS</h2>
    <h1 class="testimonials__title">Here’s what people are saying about plimbo.</h1>
    <svg class="slider-arrow slider-arrow--prev" viewBox="0 0 42 76" aria-label="Previous"><polyline points="39,2 3,38 39,74" fill="none" stroke="#111" stroke-width="3"/></svg>
    <p class="quote">“This is a testimonial where someone has writeen something amazing about plimbo. They loved it and wanted to write in and say just how great it was and that they’re telling all their friends.”</p>
    <p class="quote__author">— Daniel</p>
    <svg class="slider-arrow slider-arrow--next" viewBox="0 0 42 76" aria-label="Next"><polyline points="3,2 39,38 3,74" fill="none" stroke="#111" stroke-width="3"/></svg>
  </section>

  <div class="hero-photo" role="img" aria-label="Photo of a person sleeping peacefully in bed among soft pillows and grey blankets"></div>

  <section class="contact">
    <h2 class="eyebrow" style="top:1238px">CONTACT</h2>
    <p class="contact__intro">Do you have any questions or comments?<br>Complete the form below and we will get back to you as soon as possible.</p>
    <form class="contact-form">
      <input class="field" type="text" placeholder="Name">
      <input class="field" type="email" placeholder="Email">
      <textarea class="field field--message" placeholder="Message"></textarea>
      <button class="button button--send" type="button">SEND</button>
    </form>
  </section>

  <a class="back-to-top">
    <svg class="back-to-top__icon" viewBox="0 0 56 56"><circle cx="28" cy="28" r="28" fill="#000"/><polyline points="18,33 28,22 38,33" fill="none" stroke="#fff" stroke-width="2"/></svg>
    <span class="back-to-top__label">BACK TO TOP</span>
  </a>

  <footer class="site-footer">
    <h2 class="eyebrow" style="top:89px">MAILING LIST</h2>
    <form class="subscribe">
      <input class="subscribe__input" type="email" placeholder="Email Address">
      <button class="button button--subscribe" type="button">SUBSCRIBE</button>
    </form>
    <p class="copyright">Copyright 2017 plimbo. All rights reserved.</p>
  </footer>
</body>
</html>
```